High end Coffee Roaster needs a Label design for new Blend

We are looking for a label design for a new blend called "Cold Brew Blend". It is a blend of coffee that we use for making cold brew coffee. The blend is sold as the whole bean and ground coffee in a bag as well as pre-brewed ready to drink in a bottle. We would like the label to be elegant but fun and It must include our logo. Please check out or website brightmillroasters.com or social media @brightmillroasters for information on our company and our coffees if you need more ideas on the kind of product we offer and our style.

Requirements
Must have
• Our Company Logo. Creative design.
Should not have
• This project should NOT be a corporate company logo, Please do NOT submit a design for a company logo this is a project for a Label. We already have a logo and we are looking for a design on a label. I have uploaded several examples of what we are looking for. Those examples are from other coffee companies who have cold brew. Those are examples only to give you a better idea of what im looking for. DO NOT COPY THEM.

```html
<!DOCTYPE html>
<html lang="en">
<head>
<meta charset="utf-8">
<title>Bright Mill Roasters – Cold Brew Coffee Label</title>
<link href="https://fonts.googleapis.com/css2?family=Rokkitt:wght@800&family=Oswald:wght@500;700&family=Courier+Prime:wght@400;700&display=swap" rel="stylesheet">
<style>
  :root {
    --page-bg: #ececec;
    --label-brown: #5b3b27;
    --label-brown-deep: #4a2f1f;
    --gold: #c99a2e;
    --gold-fill: #c8961f;
    --ink-dark: #33200f;
    --cream: #f4efe6;
    --shadow: #2a1a10;
  }
  * { box-sizing: border-box; margin: 0; padding: 0; }
  html, body {
    width: 1200px; height: 1133px; overflow: hidden;
    background: var(--page-bg);
  }
  .label {
    position: absolute; left: 263px; top: 75px;
    width: 674px; height: 983px;
    background: linear-gradient(180deg, var(--label-brown) 0%, var(--label-brown-deep) 100%);
    color: var(--cream);
    overflow: hidden;
  }
  .rule {
    position: absolute; left: 0; right: 0; height: 3px;
    background: var(--gold);
  }
  .rule--top { top: 18px; }
  .rule--bottom { top: 958px; }

  .brand {
    position: absolute; left: 0; right: 0; top: 222px;
    display: flex; align-items: center; justify-content: center; gap: 16px;
    font-family: "Oswald", sans-serif; font-weight: 500;
    font-size: 38px; letter-spacing: 1px; color: var(--cream);
    white-space: nowrap;
  }
  .brand__dot {
    width: 30px; height: 30px; border-radius: 50%;
    background: var(--gold);
  }

  .title {
    position: absolute; left: 0; right: 0;
    display: flex; align-items: center; justify-content: center;
    font-family: "Rokkitt", serif; font-weight: 800;
    color: var(--cream); text-transform: uppercase;
    text-shadow: 3px 4px 0 var(--shadow);
    line-height: 1; white-space: nowrap;
  }
  .title__text { display: inline-block; }
  .title--main { top: 335px; height: 160px; font-size: 120px; }
  .title--main .title__text { letter-spacing: -2px; transform: scale(0.92, 1.3); }
  .title--sub { top: 530px; height: 110px; font-size: 82px; gap: 22px; }
  .title--sub .title__text { transform: scale(0.95, 1.25); }
  .flourish { width: 140px; height: 12px; flex: none; }

  .tagline {
    position: absolute; left: 57px; top: 676px;
    width: 561px; height: 110px;
    background: var(--gold-fill);
    border: 3px dashed var(--ink-dark);
    outline: 4px solid var(--gold-fill);
    display: flex; align-items: center; justify-content: center;
    font-family: "Oswald", sans-serif; font-weight: 700;
    font-size: 44px; letter-spacing: 1px; color: var(--ink-dark);
    white-space: nowrap;
  }

  .maker {
    position: absolute; left: 60px; top: 832px; width: 440px;
    text-align: center; font-family: "Courier Prime", monospace;
    color: var(--cream); white-space: nowrap;
  }
  .maker__line { font-size: 34px; font-weight: 700; }
  .maker__name { font-size: 28px; margin-top: 18px; }

  .volume-divider {
    position: absolute; left: 522px; top: 832px;
    width: 2px; height: 106px; background: var(--cream);
  }
  .volume {
    position: absolute; left: 540px; top: 830px; width: 80px;
    text-align: center; font-family: "Oswald", sans-serif; color: var(--cream);
  }
  .volume__amount { font-size: 44px; font-weight: 500; line-height: 1.1; }
  .volume__unit { font-size: 26px; font-weight: 500; margin-top: 4px; }
</style>
</head>
<body>
  <main class="label">
    <div class="rule rule--top"></div>

    <div class="brand">
      <span class="brand__dot"></span>
      <span class="brand__name">BRIGHT MILL ROASTERS</span>
    </div>

    <h1 class="title title--main"><span class="title__text">Cold Brew</span></h1>
    <h2 class="title title--sub">
      <svg class="flourish" viewBox="0 0 140 12"><polygon points="0,6 140,1 140,11" fill="#f4efe6"/></svg>
      <span class="title__text">Coffee</span>
      <svg class="flourish" viewBox="0 0 140 12"><polygon points="140,6 0,1 0,11" fill="#f4efe6"/></svg>
    </h2>

    <div class="tagline">PREMIUM COFFEE DRINK</div>

    <div class="maker">
      <p class="maker__line">Brewed &amp; Bottled by:</p>
      <p class="maker__name">Bright Mill Roasters</p>
    </div>
    <div class="volume-divider"></div>
    <div class="volume">
      <p class="volume__amount">32</p>
      <p class="volume__unit">FL.OZ</p>
    </div>

    <div class="rule rule--bottom"></div>
  </main>
</body>
</html>
```